Lumenvale Consulting Group

This is a new consulting business in the area of broadband technology. The logo should reflect the key aspects of our expertise - fiber optic networking and wireless high speed data.

Target Market(s)

Multi unit housing. hotel and subdivision developers, city communications authorities, ISP's

Industry/Entity Type

Telecommunications

Contact Information for Business Card

A logo that reflects the type of business

Font styles to use
Sans Serif

Colors

Designer to choose colors to be used in the design.

Requirements
Must have
• Logo, name, job title, contact info including address, cellphone number, email address and web URL (www.lumenvaleconsultinggroup.com)

```html
<!DOCTYPE html>
<html lang="en">
<head>
<meta charset="utf-8">
<title>Lumenvale Consulting Group – Business Card</title>
<link rel="stylesheet" href="https://fonts.googleapis.com/css2?family=Michroma&family=Lato:wght@400&display=swap">
<style>
  :root {
    --page-bg: #d9d4cc;
    --card-bg: #0c0d12;
    --card-glow: #1b1d2a;
    --accent: #27b8e8;
    --ink: #ffffff;
    --ink-soft: #e6e8ee;
  }
  * { box-sizing: border-box; margin: 0; padding: 0; }
  html, body {
    width: 1200px; height: 1000px; overflow: hidden;
    background: var(--page-bg);
  }
  .stage { position: relative; width: 1200px; height: 1000px; }
  .card {
    position: absolute;
    width: 700px; height: 400px;
    background: radial-gradient(ellipse at 75% 30%, var(--card-glow) 0%, var(--card-bg) 65%);
    border-radius: 4px;
    box-shadow: 0 10px 30px rgba(0,0,0,0.35);
    color: var(--ink);
  }
  .card--back { left: 110px; top: 80px; }
  .card--front { left: 390px; top: 520px; }

  .brand {
    position: absolute;
    display: flex; align-items: center; gap: 18px;
  }
  .brand__dot {
    width: 34px; height: 34px; border-radius: 50%;
    background: var(--accent);
    flex: none;
  }
  .brand__name {
    font-family: "Michroma", sans-serif;
    color: var(--accent);
    font-size: 26px;
    line-height: 1.25;
    letter-spacing: 0.5px;
  }
  .card--back .brand { left: 130px; top: 130px; }
  .card--back .site {
    position: absolute; left: 0; right: 0; top: 270px;
    text-align: center;
    font-family: "Lato", sans-serif;
    font-size: 20px; letter-spacing: 0.5px;
    color: var(--accent);
  }

  .card--front .brand { left: 60px; top: 40px; }
  .person { position: absolute; left: 60px; top: 175px; }
  .person__name {
    font-family: "Michroma", sans-serif;
    font-size: 26px; color: var(--accent);
  }
  .person__title {
    font-family: "Michroma", sans-serif;
    font-size: 17px; color: var(--ink); margin-top: 6px;
  }
  .person__domain {
    font-family: "Lato", sans-serif;
    font-size: 17px; color: var(--ink-soft); margin-top: 6px;
  }
  .contacts {
    position: absolute; left: 60px; top: 290px;
    list-style: none;
    font-family: "Lato", sans-serif; font-size: 20px;
  }
  .contacts li { display: flex; align-items: center; gap: 22px; height: 32px; }
  .contacts svg { width: 22px; height: 22px; flex: none; }
  .contacts .contact--web { color: var(--accent); }
  .contacts .contact__text { color: var(--ink-soft); }
  .contacts .contact--web .contact__text { color: var(--accent); }
</style>
</head>
<body>
<main class="stage">
  <section class="card card--back" aria-label="Card back">
    <div class="brand">
      <span class="brand__dot"></span>
      <span class="brand__name">Lumenvale<br>Consulting Group</span>
    </div>
    <p class="site">www.lumenvaleconsultinggroup.com</p>
  </section>

  <section class="card card--front" aria-label="Card front">
    <div class="brand">
      <span class="brand__dot"></span>
      <span class="brand__name">Lumenvale<br>Consulting Group</span>
    </div>
    <div class="person">
      <p class="person__name">Dana Merrow</p>
      <p class="person__title">Broadband Technology Consultant</p>
      <p class="person__domain">Lumenvaleconsultinggroup.com</p>
    </div>
    <ul class="contacts">
      <li class="contact contact--phone">
        <svg viewBox="0 0 24 24" fill="none" stroke="#27b8e8" stroke-width="2"><rect x="6" y="2" width="12" height="20" rx="2"/><line x1="11" y1="18" x2="13" y2="18"/></svg>
        <span class="contact__text">555-214-0387</span>
      </li>
      <li class="contact contact--email">
        <svg viewBox="0 0 24 24" fill="#27b8e8"><path d="M2 6h20v12H2z"/><path d="M2 6l10 7 10-7" stroke="#0c0d12" stroke-width="1.6" fill="none"/></svg>
        <span class="contact__text">dana@lumenvaleconsultinggroup.com</span>
      </li>
      <li class="contact contact--web">
        <svg viewBox="0 0 24 24" fill="none" stroke="#27b8e8" stroke-width="2.2"><path d="M10 14a4 4 0 0 0 5.6 0l3-3a4 4 0 0 0-5.6-5.6l-1 1"/><path d="M14 10a4 4 0 0 0-5.6 0l-3 3a4 4 0 0 0 5.6 5.6l1-1"/></svg>
        <span class="contact__text">www.lumenvaleconsultinggroup.com</span>
      </li>
    </ul>
  </section>
</main>
</body>
</html>
```